Website for Reiki and Wellness Courses

I teach online courses in Reiki and wellness/self-development and am needing a new website.

The focus of the website will be to provide descriptions of the courses as well as include a blog and pages where students in my courses will visit for additional information.

Note: courses are NOT hosted on this site.
The focus of this website will be to encourage viewers to enroll in courses as well as opt in to the email list.

I will upload copy soon. My old website is: http://calmstreamlessons.example. Please do not use existing logo.

Target Market(s)

Alternative health, wellness, spirituality, personal development. Males and females of all ages seeking to improve their health and life.

Industry/Entity Type

Health And Wellness

Logo Text

No text (please do not use existing logo)

Coding

Coded - Design and coding required

Number of Pages Required

5+ page

Requirements
Must have
• 1. Home page
• 2. About page
• 3. Courses page that outlines courses (there are currently 6 courses with 1 coming soon)
• 4. Individual course page (maybe a template that I can adjust color and pictures for with each course)
• 5. Blog
• 6. Student Area that outlines all Student Areas
• 7. Individual Student Area page (maybe a template that I can adjust color and pictures for with each course)
• 8. Shop page (note: items will not currently be purchased through website - it will be a link to brightmart for a book).
• 9. Student thank-you page (maybe a template that I can adjust color and pictures for with each course) this is the page students are directed to at end of course with vouchers for other courses.
• Opt-in for the home page, course pages, blog and thank-you pages
Nice to have
• I would like the design to be calm, clean and soothing. Ideally visitors feel relaxed when viewing the site and are encouraged to explore the courses, subscribe to the email list and purchase a product.
• ~ Testimonials page
• ~ Contact page
• I tend to gravitate towards blues, greys and purples as well as monochromatic color schemes.
Should not have
• Contact form on home page
• phone number on home page
• location/physical address
• dates for blog posts

```html
<!DOCTYPE html>
<html lang="en">
<head>
<meta charset="utf-8">
<title>Calm Stream Lessons</title>
<link href="https://fonts.googleapis.com/css2?family=Dosis:wght@400;500;600;700&family=Lato:wght@300;400;700&display=swap" rel="stylesheet">
<style>
:root{
  --ink:#3f4452;
  --body:#5b5f6b;
  --muted:#8a8e99;
  --accent:#6c6d8c;
  --accent-soft:#c9cad8;
  --dark:#1c1c1e;
  --darker:#111113;
  --soft-bg:#f2f4f8;
  --white:#ffffff;
  --line:#d7d9e0;
}
*{box-sizing:border-box;margin:0;padding:0}
html,body{width:1200px;height:2975px;overflow:hidden;background:var(--white)}
body{position:relative;font-family:'Lato',sans-serif;color:var(--body)}
.abs{position:absolute}
.heading{font-family:'Dosis',sans-serif;font-weight:600;color:var(--ink)}
.rule{position:absolute;height:4px;background:var(--accent-soft)}

/* top bar */
.topbar{left:0;top:0;width:1200px;height:28px;background:var(--dark)}
.topbar .welcome{position:absolute;left:58px;top:8px;font-size:10px;color:#ddd}
.social{position:absolute;top:5px;display:flex;gap:10px;right:50px}
.social span{width:18px;height:18px;border:1px solid #bbb;background:#2a2a2c}

/* hero */
.hero{left:0;top:28px;width:1200px;height:620px;background:linear-gradient(115deg,#c9a99a 0%,#d8c8bd 30%,#bfc3c4 55%,#8f9aa0 80%,#6d7478 100%)}
.clouds{left:0;top:580px;width:1200px;height:70px}
.brand{left:58px;top:48px;display:flex;align-items:center;gap:12px}
.brand .mark{width:46px;height:46px;border:3px solid var(--accent)}
.brand .name{font-family:'Dosis',sans-serif;font-weight:600;font-size:22px;color:var(--accent);line-height:1}
.nav{top:64px;right:50px;display:flex;gap:20px;font-family:'Dosis',sans-serif;font-weight:700;font-size:13px;color:var(--white);letter-spacing:.3px}
.nav .current{border-bottom:2px solid var(--white);padding-bottom:3px}
.hero-line{left:58px;top:112px;width:1092px;height:1px;background:rgba(255,255,255,.35)}

/* features */
.feature{position:absolute;top:698px;width:300px;text-align:center}
.feature .icon{width:88px;height:88px;margin:0 auto;border:2px solid var(--accent);border-radius:50%;display:flex;align-items:center;justify-content:center}
.feature h3{margin-top:44px;font-size:16px}
.feature p{margin-top:22px;font-size:12px;line-height:22px;color:var(--body)}
.feature a{color:var(--body);text-decoration:underline}

/* about */
.about{left:0;top:972px;width:1200px;height:450px;background:var(--soft-bg)}
.about h2{position:absolute;left:0;width:1200px;top:77px;text-align:center;font-size:17px}
.about .rule{left:540px;top:119px;width:120px}
.about .content{position:absolute;left:350px;top:150px;width:500px;text-align:center}
.about .copy{font-size:12px;line-height:22px}
.about .copy p+p{margin-top:22px}
.btn-outline{border:2px solid var(--accent);border-radius:22px;font-family:'Dosis',sans-serif;font-weight:600;font-size:15px;color:var(--accent);display:flex;align-items:center;justify-content:center}
.about .btn-outline{width:152px;height:41px;margin:26px auto 0}
.photo-students-left{left:0;top:138px;width:330px;height:312px;background:linear-gradient(160deg,#e9d6c3,#c9b199 55%,#6d8cae)}
.photo-students-right{left:868px;top:0;width:332px;height:450px;background:linear-gradient(160deg,#eadccc,#c7ab92 50%,#5f7fa6)}

/* courses */
.courses-title{left:131px;top:1462px;font-size:16px}
.course-card{position:absolute;top:1529px;width:256px;height:266px;background:#ececee}
.course-card .img{width:256px;height:216px}
.course-card .cap{position:absolute;left:16px;top:232px;font-family:'Dosis',sans-serif;font-weight:600;font-size:13px;color:var(--ink)}
.arrow{position:absolute;width:32px;height:32px;border-radius:50%;background:var(--accent);display:flex;align-items:center;justify-content:center}
.feature-card{left:696px;top:1467px;width:373px;height:464px;border:1px solid var(--line);background:var(--white)}
.feature-card .img{position:absolute;left:-1px;top:-1px;width:373px;height:247px;background:linear-gradient(160deg,#b98fc2,#cda0b8 45%,#b8a985 100%)}
.feature-card .overlay{position:absolute;right:26px;top:22px;text-align:right;font-family:'Dosis',sans-serif;color:var(--white);font-weight:600}
.feature-card .overlay .big{font-size:30px;letter-spacing:1.5px}
.feature-card .overlay .small{font-size:17px;line-height:34px;letter-spacing:.8px}
.feature-card h3{position:absolute;left:21px;top:268px;font-size:15px;color:var(--accent)}
.feature-card .rule{left:21px;top:297px;width:330px;height:3px}
.feature-card p{position:absolute;left:21px;top:320px;width:320px;font-size:12px;line-height:23px}
.feature-card .btn-outline{position:absolute;left:21px;top:404px;width:140px;height:41px;border-radius:3px}

/* testimonial */
.testimonials{left:0;top:1977px;width:1200px;height:413px;background:linear-gradient(120deg,#2b2320,#161416 45%,#0e0e10)}
.testimonials h2{position:absolute;width:1200px;top:76px;text-align:center;color:var(--white);font-size:16px}
.testimonials .rule{left:554px;top:108px;width:92px;background:#555}
.testimonials .content{position:absolute;left:290px;top:134px;width:620px;text-align:center}
.testimonials .lead{font-size:16px;line-height:22px;color:#e8e8e8;font-weight:300}
.testimonials .quote{margin-top:4px;font-size:12px;line-height:22px;color:#e2e2e2}
.testimonials .who{margin-top:12px;font-family:'Dosis',sans-serif;font-weight:700;font-size:11px;color:var(--white);letter-spacing:.5px}
.dots{margin-top:16px;display:flex;justify-content:center;gap:6px}
.dots span{width:10px;height:10px;border-radius:50%;background:#bbb}
.dots span:first-child{background:var(--white)}

/* opt-in */
.optin-title{left:131px;top:2432px;font-size:16px}
.optin-rule{left:131px;top:2462px;width:90px}
.optin-copy{left:131px;top:2494px;width:440px;font-size:12px;line-height:23px}
.form{left:617px;top:2435px;width:452px;height:335px;border:1px solid var(--line)}
.form label{position:absolute;left:32px;font-family:'Dosis',sans-serif;font-weight:700;font-size:12px;color:var(--accent)}
.form .field{position:absolute;left:32px;width:384px;height:30px;border:1px solid #c7c9d0;background:var(--white)}
.form .submit{position:absolute;left:32px;top:267px;width:384px;height:34px;background:var(--accent);color:var(--white);font-family:'Dosis',sans-serif;font-weight:700;font-size:12px;display:flex;align-items:center;justify-content:center}

/* footer */
.footer{left:0;top:2816px;width:1200px;height:115px;background:var(--dark)}
.footer nav{position:absolute;width:1200px;top:47px;display:flex;justify-content:center;gap:20px;font-family:'Dosis',sans-serif;font-weight:500;font-size:13px;color:#e4e4e4}
.footer nav .current{color:var(--muted)}
.copyright{left:0;top:2931px;width:1200px;height:44px;background:var(--darker);text-align:center;font-size:10px;color:#ccc;line-height:44px}
</style>
</head>
<body>

<div class="abs topbar">
  <div class="welcome">Welcome to Calm Stream Lessons</div>
  <div class="social"><span></span><span></span><span></span><span></span><span></span></div>
</div>

<div class="abs hero" role="img" aria-label="Photo of a man working on a laptop showing a business plan"></div>
<svg class="abs clouds" viewBox="0 0 1200 70" preserveAspectRatio="none" aria-hidden="true">
  <path fill="#ffffff" d="M0 40 Q30 10 70 30 Q100 5 140 28 Q180 8 220 30 Q260 12 300 32 Q340 6 385 30 Q425 10 465 32 Q505 4 550 28 Q590 12 630 30 Q670 6 715 28 Q755 10 795 30 Q835 4 880 28 Q920 12 960 32 Q1000 6 1045 30 Q1085 10 1125 30 Q1165 14 1200 34 L1200 70 L0 70 Z"/>
</svg>
<div class="abs brand">
  <div class="mark"></div>
  <div class="name">Calm Stream<br>Lessons</div>
</div>
<nav class="abs nav">
  <span class="current">HOME</span><span>ABOUT</span><span>COURSES</span><span>BLOG</span><span>STUDENT AREAS</span><span>CONTACT</span>
</nav>
<div class="abs hero-line"></div>

<section>
  <div class="feature" style="left:128px">
    <div class="icon"><svg width="40" height="40" viewBox="0 0 40 40" fill="none" stroke="#6c6d8c" stroke-width="2"><rect x="6" y="8" width="28" height="22"/><path d="M10 24l6-6 5 4 8-9"/><path d="M6 34h28"/></svg></div>
    <h3 class="heading">How Reiki Works</h3>
    <p>Reiki has been used for centuries to help individuals with physical and emotional imbalances as well as those seeking clarity and enlightenment.</p>
  </div>
  <div class="feature" style="left:450px">
    <div class="icon"><svg width="40" height="40" viewBox="0 0 40 40" fill="none" stroke="#6c6d8c" stroke-width="2"><path d="M10 5h16l6 6v24H10z"/><path d="M15 14h10M15 19h12M15 24h8"/><circle cx="26" cy="30" r="3"/></svg></div>
    <h3 class="heading">Traditional Usui Reiki Master Certification</h3>
    <p>Become a Certified Reiki Master with an interactive online course. In the Reiki Levels I, II and Master online course – through text, images and videos …<a>Read More</a></p>
  </div>
  <div class="feature" style="left:772px">
    <div class="icon"><svg width="40" height="40" viewBox="0 0 40 40" fill="#6c6d8c"><rect x="6" y="8" width="5" height="24"/><rect x="13" y="8" width="5" height="24"/><rect x="20" y="8" width="4" height="24"/><path d="M26 9l4-1 5 23-4 1z"/></svg></div>
    <h3 class="heading">Resources</h3>
    <p>Information and tools to help you create a life you love.<br><a>Read More</a></p>
  </div>
</section>

<section class="abs about">
  <div class="abs photo-students-left" role="img" aria-label="Photo of two smiling students holding books"></div>
  <div class="abs photo-students-right" role="img" aria-label="Photo of two smiling students with backpacks and books"></div>
  <h2 class="heading">About Calm Stream Lessons</h2>
  <div class="rule"></div>
  <div class="content">
    <div class="copy">
      <p>Thought to be centuries old and rediscovered in the late 1800's, Reiki (pronounced ray-key) is a healing and enlightenment system. Reiki can be translated into "Universal (Rei) Life Energy (Ki)". As a practitioner of Reiki, you attune your awareness to this energy and utilize it for the physical and emotional healing of self and others.</p>
      <p>Reiki is non-denominational and can be practiced by everyone, regardless of their religious and spiritual beliefs. Reiki can be performed hands-on in person or from a distance.</p>
    </div>
    <div class="btn-outline">Read More</div>
  </div>
</section>

<section>
  <h2 class="abs heading courses-title">Our Online Courses</h2>
  <div class="rule" style="left:131px;top:1495px;width:120px"></div>
  <div class="course-card" style="left:131px">
    <div class="img" role="img" aria-label="Photo of pets peeking over a ledge" style="background:linear-gradient(180deg,#f4f4f4,#e3ddd6)"></div>
    <div class="cap">Animal Reiki Practitioner Certification</div>
  </div>
  <div class="course-card" style="left:412px">
    <div class="img" role="img" aria-label="Photo of a hands-on healing session" style="background:linear-gradient(150deg,#e8ddd3,#c9b3a2)"></div>
    <div class="cap">Build Your Reiki Business</div>
  </div>
  <div class="arrow" style="left:147px;top:1634px"><svg width="12" height="12" viewBox="0 0 12 12"><path d="M8 2L4 6l4 4" stroke="#fff" stroke-width="2" fill="none"/></svg></div>
  <div class="arrow" style="left:620px;top:1634px"><svg width="12" height="12" viewBox="0 0 12 12"><path d="M4 2l4 4-4 4" stroke="#fff" stroke-width="2" fill="none"/></svg></div>

  <div class="abs feature-card">
    <div class="img" role="img" aria-label="Photo of two wooden chairs in soft purple light"></div>
    <div class="overlay"><div class="big">Reiki</div><div class="small">Levels I, II and<br>Master online course</div></div>
    <h3 class="heading">Reiki Levels I, II and Master online course</h3>
    <div class="rule"></div>
    <p>Become a Certified Reiki Master with an interactive online course. In the Reiki Levels I, II and Master online course – through text, images and videos you will learn about:</p>
    <div class="btn-outline">Read More</div>
  </div>
</section>

<section class="abs testimonials" role="img" aria-label="Dark softly blurred photo background behind student testimonial">
  <h2 class="heading">Our Students Say</h2>
  <div class="rule"></div>
  <div class="content">
    <div class="lead">This course changed my life in wonderful ways!</div>
    <div class="quote">I was drawn to this course with the desire to heal family, friends and pets and this course has given me that ability and more. With it, Reiki has healed me on many levels and given me insight into my own spirituality and to what is possible. The continued contact with Maya Linden on the Circlebook group page as well as input and questions and answers from other students of the course are educational and enlightening and I learn more from every answer Maya Linden gives. I highly recommend the Reiki Level I, II, and Master Certification course by Maya Linden.</div>
    <div class="who">DANA WHITFIELD</div>
    <div class="dots"><span></span><span></span><span></span><span></span></div>
  </div>
</section>
<svg class="abs" style="left:0;top:1970px" width="1200" height="40" viewBox="0 0 1200 40" preserveAspectRatio="none" aria-hidden="true"><path fill="#fff" d="M0 0H1200V7Q600 70 0 7Z"/></svg>
<svg class="abs" style="left:0;top:2352px" width="1200" height="40" viewBox="0 0 1200 40" preserveAspectRatio="none" aria-hidden="true"><path fill="#fff" d="M0 40H1200V38Q600 -20 0 38Z"/></svg>

<section>
  <h2 class="abs heading optin-title">Stay Inspired</h2>
  <div class="rule optin-rule"></div>
  <p class="abs optin-copy">Receive information and articles each month to keep you feeling inspired. As a thank-you, you will also receive access to soothing music you can download for use in your Reiki sessions and meditation.</p>
  <form class="abs form">
    <label style="top:32px">FIRST NAME *</label><div class="field" style="top:56px"></div>
    <label style="top:107px">LAST NAME *</label><div class="field" style="top:131px"></div>
    <label style="top:181px">EMAIL *</label><div class="field" style="top:205px"></div>
    <div class="submit">YES - COUNT ME IN</div>
  </form>
</section>

<footer class="abs footer">
  <nav><span class="current">HOME</span><span>ABOUT</span><span>COURSES</span><span>BLOG</span><span>STUDENT AREAS</span><span>CONTACT</span></nav>
</footer>
<div class="abs copyright">Copyright © 2016 Calm Stream Lessons. | All Rights Reserved.</div>

</body>
</html>
```